PowerPoint Template for Regional Harmony Institute. Website is www.regionalharmonyinstitute.com

The tagline for the Center is "Connecting the brightest minds in healthcare"

```html
<!DOCTYPE html>
<html lang="en">
<head>
<meta charset="utf-8">
<title>Regional Harmony Institute – Presentation Template</title>
<link rel="stylesheet" href="https://fonts.googleapis.com/css2?family=Nunito+Sans:wght@400;600;700;800&display=swap">
<style>
  :root {
    --page-bg: #e6e6e6;
    --slide-bg: #ffffff;
    --brand-blue: #0a86c9;
    --brand-navy: #17507f;
    --deep-navy: #0d3f66;
    --sky-blue: #45a8d6;
    --text-dark: #1b1b1b;
    --map-light: #eef0f2;
    --map-mid: #d3d7db;
  }
  * { box-sizing: border-box; margin: 0; padding: 0; }
  html, body {
    width: 1200px; height: 900px; overflow: hidden;
    background: var(--page-bg);
    font-family: "Nunito Sans", Arial, sans-serif;
  }
  .deck { position: relative; width: 1200px; height: 900px; }
  .slide {
    position: absolute; width: 436px; height: 326px;
    background: var(--slide-bg);
    border-bottom: 5px solid var(--brand-blue);
    overflow: hidden;
  }
  .slide--cover { left: 146px; top: 105px; }
  .slide--network { left: 612px; top: 105px; }
  .slide--chart { left: 146px; top: 469px; }
  .slide--text { left: 612px; top: 469px; }

  .body-copy {
    font-size: 9.6px; line-height: 12px; font-weight: 600;
    color: var(--text-dark);
  }
  .body-copy strong { font-weight: 800; }

  /* cover */
  .cover-title {
    position: absolute; left: 62px; top: 86px;
    display: flex; align-items: center; gap: 6px;
    font-size: 18px; font-weight: 600; color: var(--brand-navy);
  }
  .cover-title::before {
    content: ""; width: 26px; height: 2px; background: var(--brand-blue);
  }
  .slide--cover .body-copy {
    position: absolute; left: 0; right: 0; top: 150px; text-align: center;
  }
  .cover-button {
    position: absolute; left: 134px; top: 226px; width: 150px; height: 25px;
    border: 1px solid var(--brand-navy);
    display: flex; align-items: center; justify-content: center;
    font-size: 15px; font-weight: 600; color: var(--brand-navy);
  }

  /* network */
  .network-visual {
    position: absolute; left: 0; top: 30px; width: 100%; height: 189px;
    background: radial-gradient(ellipse at 45% 50%, var(--map-light) 0%, var(--map-mid) 100%);
  }
  .accent-rule { position: absolute; height: 1px; background: var(--brand-blue); }
  .slide--network .accent-rule { left: 68px; top: 246px; width: 27px; }
  .slide--network .body-copy { position: absolute; left: 68px; top: 252px; }

  /* chart */
  .chart-title {
    position: absolute; left: 46px; top: 48px;
    font-size: 18px; font-weight: 600; color: var(--brand-navy);
  }
  .chart-rule {
    position: absolute; left: 46px; right: 0; top: 76px; height: 1px;
    background: var(--brand-navy);
  }
  .pie-chart { position: absolute; left: 142px; top: 98px; }
  .slide--chart .body-copy {
    position: absolute; left: 0; right: 0; top: 270px; text-align: center;
  }

  /* text */
  .slide--text .accent-rule { left: 204px; width: 28px; }
  .slide--text .accent-rule--top { top: 114px; }
  .slide--text .accent-rule--bottom { top: 221px; }
  .slide--text .body-copy {
    position: absolute; left: 66px; right: 66px; top: 120px;
    text-align: center; line-height: 12px;
  }
</style>
</head>
<body>
<main class="deck">
  <section class="slide slide--cover">
    <h1 class="cover-title">The Regional Harmony Institute</h1>
    <p class="body-copy">Lorem ipsum dolor sit amet, consectetuer adipiscing elit, sed diam<br>nonummy nibh euismod <strong>tincidunt ut laoreet</strong> dolore magna</p>
    <div class="cover-button">Lorem ipsum</div>
  </section>

  <section class="slide slide--network">
    <div class="network-visual" role="img" aria-label="Soft grey map of the country with a hub of healthcare icons connected around a central emblem"></div>
    <span class="accent-rule"></span>
    <p class="body-copy">Lorem ipsum dolor sit amet, consectetuer adipiscing elit, sed diam<br>nonummy nibh euismod tincidunt ut laoreet dolore magna</p>
  </section>

  <section class="slide slide--chart">
    <h2 class="chart-title">The Regional Harmony Institute</h2>
    <span class="chart-rule"></span>
    <svg class="pie-chart" width="152" height="152" viewBox="-76 -76 152 152" role="img" aria-label="Pie chart with three segments">
      <path d="M0 0 L59.9 -46.8 A76 76 0 1 1 0 -76 Z" fill="var(--brand-blue)"/>
      <path d="M0 0 L0 -76 A76 76 0 0 1 23.5 -72.3 Z" fill="var(--deep-navy)"/>
      <path d="M0 0 L23.5 -72.3 A76 76 0 0 1 59.9 -46.8 Z" fill="var(--sky-blue)"/>
    </svg>
    <p class="body-copy">Lorem ipsum dolor sit amet, consectetuer adipiscing elit, sed diam<br>nonummy nibh euismod <strong>tincidunt ut laoreet</strong> dolore magna</p>
  </section>

  <section class="slide slide--text">
    <span class="accent-rule accent-rule--top"></span>
    <p class="body-copy">Lorem ipsum dolor sit amet, consectetuer adipiscing elit, sed diam nonummy nibh euismod tincidunt ut laoreet dolore magna aliquam erat volutpat. Ut wisi enim ad minim veniam, quis nostrud exerci tation ullamcorper suscipit lobortis nisl ut aliquip ex ea commodo consequat. Duis autem vel eum iriure dolor in hendrerit in vulputate velit esse molestie consequat, vel illum dolore eu feugiat nulla facilisis at vero eros et accumsan et iusto odio dignissim qui blandit praesent luptatum zzril delenit augue duis</p>
    <span class="accent-rule accent-rule--bottom"></span>
  </section>
</main>
</body>
</html>
```